Aquatic View

We need a web design for a new window cleaning company name Tidal Pane Care. We are located in Grand Cayman, Cayman Islands. We are a small company, a team of husband and wife. Our services include residencial interior and exterior window cleaning and commercial. Extra services such as ceiling fans cleaning, mirrors, high dusting. Home cleaning services. Power washing. Explaining the service. We want a modern, beachy style with aquatic colors. We want to use our domain name "tidalpanecare.ky". We want to portray a clean, modern and professional design.

Target Market(s)

Big Home owners

Industry/Entity Type

Cleaning Service

Contact Information for Business Card

Company Name: Tidal Pane Care
Name: Dennis Okafor owner/manager
Phone: 345-5550194
Email: dennis@tidalpanecare.ky
Website: tidalpanecare.ky
Address: P.O.Box 4820 GT, George Town, Grand Cayman KY1-2043 Cayman Islands

Number of Pages Required

2 page

Font styles to use
Sans Serif

Colors
0592cd
0455a3
33a6d7
85cae6
cadf82
abd036
fbf289

Requirements
Nice to have
• Pictures of an ocean view and palm trees from clear windows.
• https://quelvaro.com/bidmatic/
• Use the above for "free estimate".

```html
<!DOCTYPE html>
<html lang="en">
<head>
<meta charset="utf-8">
<title>Tidal Pane Care</title>
<link rel="stylesheet" href="https://fonts.googleapis.com/css2?family=Open+Sans:wght@400;600;700&display=swap">
<style>
:root{
  --ocean:#0592cd;
  --deep:#0455a3;
  --sky:#33a6d7;
  --mist:#85cae6;
  --lime-soft:#cadf82;
  --lime:#abd036;
  --sun:#fbf289;
  --ink:#2b2b2b;
  --grey:#6b6b6b;
  --line:#dcdcdc;
  --paper:#f4f4f4;
  --tint:#eaf2cf;
  --navy:#0a4c96;
  --navy-dark:#083d7a;
}
*{box-sizing:border-box;margin:0;padding:0}
html,body{width:1200px;height:5000px;overflow:hidden}
body{font-family:"Open Sans",Arial,sans-serif;color:var(--ink);background:#fff;font-size:14px;line-height:1.55}
.wrap{width:880px;margin:0 auto;position:relative;height:100%}
.sect-title{font-size:34px;font-weight:400;color:var(--ocean);text-align:center;line-height:1.2}
.sect-sub{font-size:17px;color:var(--grey);text-align:center}
.rule{width:60px;height:3px;background:var(--ocean);margin:10px auto 0}

/* header */
.site-header{height:110px;position:relative;background:#fff}
.brand{position:absolute;left:0;top:28px;display:flex;align-items:center;gap:12px}
.brand-dot{width:44px;height:44px;border-radius:50%;background:var(--ocean)}
.brand-name{font-size:26px;font-weight:700;color:var(--deep)}
.topline{position:absolute;right:0;top:14px;font-size:13px;display:flex;gap:26px;color:var(--ink)}
.topline span{display:flex;align-items:center;gap:6px}
.nav{position:absolute;right:0;top:66px;display:flex;gap:22px;font-size:15px;color:var(--ocean)}

/* hero */
.hero{height:535px;position:relative;background:linear-gradient(90deg,#3f7ea6 0%,#7fb4d4 35%,#cfe6f2 70%,#eef6fa 100%)}
.hero-copy{position:absolute;left:160px;top:120px;width:430px}
.hero-copy h1{font-size:32px;font-weight:700;color:#fff;line-height:1.35}
.btn-about{display:inline-block;margin-top:22px;background:var(--deep);color:#fff;font-weight:700;font-size:16px;padding:10px 22px;border-radius:4px}
.estimate{position:absolute;left:160px;top:420px;width:210px;height:88px;background:var(--ocean);border-radius:10px;color:#fff;display:flex;align-items:center;padding-left:18px}
.estimate b{font-size:26px;line-height:1.05;font-weight:700}
.estimate i{position:absolute;right:14px;top:14px;width:60px;height:60px;border-radius:50%;background:var(--deep);font-style:normal;font-size:12px;font-weight:700;text-align:center;line-height:1.1;display:flex;align-items:center;justify-content:center;border:2px solid #fff}
.slide-arrow{position:absolute;top:235px;width:30px;height:60px;background:var(--deep);display:flex;align-items:center;justify-content:center}
.slide-arrow.l{left:0}.slide-arrow.r{right:0}

/* about */
.about{height:472px;padding-top:22px}
.about-body{margin-top:28px;position:relative;font-size:12.5px;color:var(--grey);line-height:1.6}
.about-photo{float:left;width:210px;height:160px;margin:0 20px 10px 0;background:linear-gradient(160deg,#d8ecf6,#8fc2de 60%,#5e98c0)}
.read-more{display:block;margin-top:12px;font-size:13px;color:var(--ink);font-weight:600}

/* services */
.services{height:1816px;background:var(--paper);padding-top:30px}
.svc{position:absolute;left:0;width:880px;height:200px;background:#fff;box-shadow:0 1px 4px rgba(0,0,0,.15)}
.svc-img{position:absolute;top:0;width:260px;height:200px}
.svc-num{position:absolute;top:60px;width:78px;height:78px;color:#fff;font-size:44px;font-weight:400;display:flex;align-items:center;justify-content:center}
.svc-text{position:absolute;top:30px;width:520px}
.svc-text h3{font-size:16px;font-weight:700;margin-bottom:8px}
.svc-text p{font-size:12.5px;color:var(--grey);line-height:1.55}
.svc-text a{display:block;margin-top:12px;font-size:12.5px;color:var(--ink)}
.svc.left .svc-img{left:0}.svc.left .svc-num{left:222px}.svc.left .svc-text{left:310px}
.svc.right .svc-img{right:0}.svc.right .svc-num{right:222px}.svc.right .svc-text{left:50px}

/* consultation */
.consult{height:733px;position:relative;background:linear-gradient(180deg,#2f7fc4 0%,#6ab0df 40%,#bfe1f2 75%,#e6f3fa 100%)}
.door{position:absolute;top:60px;width:230px;height:620px;background:linear-gradient(180deg,#f4f7f9,#d9e3ea)}
.door.l{left:0}.door.r{right:0}
.consult-head{position:absolute;top:45px;left:0;right:0;text-align:center;color:#fff}
.consult-head h2{font-size:34px;font-weight:400}
.consult-head p{font-size:17px}
.chev{width:52px;height:52px;border-radius:50%;border:2px solid #fff;margin:10px auto 0;display:flex;align-items:center;justify-content:center;background:rgba(4,85,163,.5)}
.panel{position:absolute;left:360px;top:227px;width:533px;height:423px;background:rgba(255,255,255,.93);padding:26px 40px}
.panel-close{position:absolute;right:-14px;top:-14px;width:36px;height:36px;border-radius:50%;background:#111;border:2px solid #fff;display:flex;align-items:center;justify-content:center}
.panel-intro{font-size:12.5px;color:var(--grey);text-align:center;line-height:1.5;margin-bottom:16px}
.field{height:38px;border:1px solid var(--line);background:#fff;margin-bottom:12px;font-size:12.5px;color:#999;padding:0 12px;display:flex;align-items:center;width:380px;position:relative}
.field.active{border-color:var(--lime)}
.field .drop{position:absolute;right:-1px;top:-1px;width:36px;height:38px;background:var(--ocean);display:flex;align-items:center;justify-content:center}
.dates-label{font-size:11px;color:var(--grey);margin-left:200px}
.submit-row{display:flex;align-items:center;gap:16px;margin-top:4px;font-size:12.5px}
.btn-submit{background:var(--ocean);color:#fff;font-weight:700;padding:9px 18px;font-size:13px}

/* testimonials */
.testimonials{height:467px;background:var(--tint);padding-top:32px}
.client-photo{position:absolute;left:0;top:140px;width:230px;height:230px;border-radius:50%;background:linear-gradient(160deg,#cfe1ea,#8fb7c9);border:6px solid #fff}
.quote{position:absolute;left:290px;top:150px;width:580px}
.quote-mark{position:absolute;left:-30px;top:-6px;font-size:40px;color:var(--ink);line-height:1}
.quote p{font-size:18px;color:var(--ink);line-height:1.5}
.quote h4{margin-top:30px;font-size:20px;color:var(--ocean);font-weight:700}
.quote small{font-size:12px;color:var(--grey)}
.dots{position:absolute;left:0;right:0;top:394px;display:flex;justify-content:center;gap:10px}
.dots i{width:16px;height:16px;border-radius:50%;background:#9a9a9a}
.dots i.on{background:var(--deep)}

/* partners */
.partners{height:250px;padding-top:22px}
.partner-row{position:absolute;top:120px;left:0;right:0;display:flex;justify-content:space-between;align-items:center;padding:0 40px}
.partner{display:flex;align-items:center;gap:10px;font-size:26px;font-weight:600;color:var(--grey)}
.partner span{width:34px;height:34px;border-radius:50%;background:var(--mist)}
.p-arrow{position:absolute;top:125px;width:26px;height:26px;border-radius:50%;background:var(--lime);display:flex;align-items:center;justify-content:center}
.p-arrow.l{left:0}.p-arrow.r{right:0}

/* contact */
.contact{height:567px;background:var(--navy);color:#fff;padding-top:80px}
.contact .sect-title{color:#fff}
.contact .sect-sub{color:#d5e4f4;font-size:14px}
.contact .rule{background:#fff;width:40px}
.office{position:absolute;left:0;top:210px;width:360px;font-size:14px}
.office h5{font-size:15px;font-weight:700;margin-bottom:4px}
.office .row{display:flex;gap:10px;margin-top:16px;align-items:flex-start}
.socials{display:flex;gap:12px;margin-top:22px}
.socials i{width:30px;height:30px;border-radius:50%;background:#fff}
.cform{position:absolute;left:465px;top:258px;width:415px}
.cform .two{display:flex;gap:10px}
.cinput{height:42px;background:#fff;color:#888;font-size:13px;padding:0 12px;display:flex;align-items:center;flex:1}
.carea{height:140px;background:#fff;color:#888;font-size:13px;padding:10px 12px;margin-top:12px}
.btn-send{display:inline-block;margin-top:14px;background:var(--ocean);color:#fff;padding:10px 44px;font-size:14px}
.to-top{position:absolute;right:-120px;top:460px;width:44px;height:44px;background:var(--ocean);display:flex;align-items:center;justify-content:center}
.site-footer{height:33px;background:var(--ocean);color:#fff;font-size:12px;text-align:center;line-height:33px}
</style>
</head>
<body>

<header class="site-header">
  <div class="wrap">
    <div class="brand"><span class="brand-dot"></span><span class="brand-name">Tidal Pane Care</span></div>
    <div class="topline">
      <span><svg width="12" height="12" viewBox="0 0 24 24"><path fill="#0455a3" d="M6.6 10.8a15 15 0 0 0 6.6 6.6l2.2-2.2c.3-.3.7-.4 1-.2 1.1.4 2.3.6 3.6.6.6 0 1 .4 1 1V20c0 .6-.4 1-1 1A17 17 0 0 1 3 4c0-.6.4-1 1-1h3.5c.6 0 1 .4 1 1 0 1.3.2 2.5.6 3.6.1.3 0 .7-.2 1z"/></svg>+345 555 0194</span>
      <span><svg width="13" height="11" viewBox="0 0 24 18"><rect x="1" y="1" width="22" height="16" fill="none" stroke="#0455a3" stroke-width="2"/><path d="M1 1l11 9 11-9" fill="none" stroke="#0455a3" stroke-width="2"/></svg>info@tidalpanecare.ky</span>
    </div>
    <nav class="nav"><span>Home</span><span>About Us</span><span>Services</span><span>Clients</span><span>Testimonials</span><span>Contact</span></nav>
  </div>
</header>

<section class="hero" role="img" aria-label="Bright living room with a white sofa and tall clear windows opening onto the sea">
  <div class="slide-arrow l"><svg width="12" height="20" viewBox="0 0 12 20"><path d="M10 2 2 10l8 8" fill="none" stroke="#fff" stroke-width="2.5"/></svg></div>
  <div class="slide-arrow r"><svg width="12" height="20" viewBox="0 0 12 20"><path d="M2 2l8 8-8 8" fill="none" stroke="#fff" stroke-width="2.5"/></svg></div>
  <div class="hero-copy">
    <h1>Our Services Include Residencial Interior And Exterior Window Cleaning And Commercial</h1>
    <span class="btn-about">ABOUT US</span>
  </div>
  <div class="estimate"><b>FREE<br>ESTIMATE</b><i>Request<br>Now!</i></div>
</section>

<section class="about">
  <div class="wrap">
    <h2 class="sect-title">About Us</h2>
    <p class="sect-sub">Tidal Pane Care, We are located in Grand Cayman, Cayman Islands</p>
    <div class="about-body">
      <div class="about-photo" role="img" aria-label="Cleaner wiping a tall glass window"></div>
      <p>We are a small company, a team of husband and wife. Our services include residencial interior and exterior window cleaning and commercial. Extra services such as ceiling fans cleaning, mirrors, high dusting. Home cleaning services. Power washing. Explaining the service. Lorem Ipsum is simply dummy text of the printing and typesetting industry. Lorem Ipsum has been the industry's standard dummy text ever since the 1500s, when an unknown printer took a galley of type and scrambled. Lorem Ipsum is simply dummy text of the printing and typesetting industry. Lorem Ipsum has been the industry's standard dummy text ever since the 1500s, when an unknown printer took a galley of type and scrambled. Lorem Ipsum is simply dummy text of the printing and typesetting industry. Lorem Ipsum has been the industry. Lorem Ipsum is simply dummy text of the printing and typesetting industry. Lorem Ipsum has been the industry's Lorem Ipsum is simply dummy text of the printing and typesetting industry. Lorem Ipsum has been the industry's Lorem Ipsum is simply dummy text of the printing and typesetting industry. Lorem Ipsum has been the industry's Lorem Ipsum is simply dummy text of the printing and typesetting industry. Lorem Ipsum has been the industry's Lorem Ipsum is simply dummy text of the printing and typesetting industry. Lorem Ipsum has been the industry's Lorem Ipsum is simply dummy text of the printing and typesetting industry. Lorem Ipsum has been the industry's Lorem Ipsum is simply dummy text of the printing and typesetting industry.</p>
      <span class="read-more">Read More...</span>
    </div>
  </div>
</section>

<section class="services">
  <div class="wrap">
    <h2 class="sect-title">Our Services</h2>
    <p class="sect-sub">Check Our Operation step by step ( how we do it )</p>
    <div class="rule"></div>

    <article class="svc left" style="top:130px">
      <div class="svc-img" role="img" aria-label="Worker washing an exterior window" style="background:linear-gradient(160deg,#9fb8c8,#4d6f85)"></div>
      <div class="svc-num" style="background:var(--ocean)">1</div>
      <div class="svc-text"><h3>Residencial Interior And Exterior Window Cleaning</h3><p>Lorem Ipsum is simply dummy text of the printing and typesetting industry. Lorem Ipsum has been the industry's Lorem Ipsum is simply dummy text of the printing and typesetting industry. Lorem Ipsum has been the industry's Lorem Ipsum is simply dummy text of the printing and typesetting industry. Lorem Ipsum has been the industry's.</p><a>Read More...</a></div>
    </article>

    <article class="svc right" style="top:370px">
      <div class="svc-img" role="img" aria-label="Window cleaner on a lift at a glass office building" style="background:linear-gradient(160deg,#2f79b8,#0b3f78)"></div>
      <div class="svc-num" style="background:var(--deep)">2</div>
      <div class="svc-text"><h3>Commercial Window Cleaning</h3><p>Lorem Ipsum is simply dummy text of the printing and typesetting industry. Lorem Ipsum has been the industry's Lorem Ipsum is simply dummy text of the printing and typesetting industry. Lorem Ipsum has been the industry's Lorem Ipsum is simply dummy text of the printing and typesetting industry.</p><a>Read More...</a></div>
    </article>

    <article class="svc left" style="top:610px">
      <div class="svc-img" role="img" aria-label="Yellow duster cleaning a ceiling fan" style="background:linear-gradient(160deg,#efe2a2,#c9a53c)"></div>
      <div class="svc-num" style="background:var(--sky)">3</div>
      <div class="svc-text"><h3>Ceiling Fans Cleaning</h3><p>Lorem Ipsum is simply dummy text of the printing and typesetting industry. Lorem Ipsum has been the industry's Lorem Ipsum is simply dummy text of the printing and typesetting industry. Lorem Ipsum has been the industry's Lorem Ipsum is simply dummy text of the printing and typesetting industry.</p><a>Read More...</a></div>
    </article>

    <article class="svc right" style="top:850px">
      <div class="svc-img" role="img" aria-label="Cleaner polishing a mirror" style="background:linear-gradient(160deg,#cfe6ee,#7fb0c4)"></div>
      <div class="svc-num" style="background:var(--mist)">4</div>
      <div class="svc-text"><h3>Mirrors Cleaning</h3><p>Lorem Ipsum is simply dummy text of the printing and typesetting industry. Lorem Ipsum has been the industry's Lorem Ipsum is simply dummy text of the printing and typesetting industry. Lorem Ipsum has been the industry's Lorem Ipsum is simply dummy text of the printing and typesetting industry.</p><a>Read More...</a></div>
    </article>

    <article class="svc left" style="top:1090px">
      <div class="svc-img" role="img" aria-label="Cleaner dusting high shelves in a bright room" style="background:linear-gradient(160deg,#efe8dc,#b9a78e)"></div>
      <div class="svc-num" style="background:var(--lime-soft)">5</div>
      <div class="svc-text"><h3>High Dusting</h3><p>Lorem Ipsum is simply dummy text of the printing and typesetting industry. Lorem Ipsum has been the industry's Lorem Ipsum is simply dummy text of the printing and typesetting industry. Lorem Ipsum has been the industry's Lorem Ipsum is simply dummy text of the printing and typesetting industry. Lorem Ipsum has been the industry's.</p><a>Read More...</a></div>
    </article>

    <article class="svc right" style="top:1330px">
      <div class="svc-img" role="img" aria-label="Gloved hand spraying cleaner on a surface" style="background:linear-gradient(160deg,#f3efe6,#d98a3a 70%,#7a4aa8)"></div>
      <div class="svc-num" style="background:var(--lime)">6</div>
      <div class="svc-text"><h3>Home Cleaning Services</h3><p>Lorem Ipsum is simply dummy text of the printing and typesetting industry. Lorem Ipsum has been the industry's Lorem Ipsum is simply dummy text of the printing and typesetting industry. Lorem Ipsum has been the industry's Lorem Ipsum is simply dummy text of the printing and typesetting industry.</p><a>Read More...</a></div>
    </article>

    <article class="svc left" style="top:1570px">
      <div class="svc-img" role="img" aria-label="Worker power washing a patio" style="background:linear-gradient(160deg,#9bb4c4,#56707f)"></div>
      <div class="svc-num" style="background:var(--sun)">7</div>
      <div class="svc-text"><h3>Power washing</h3><p>Lorem Ipsum is simply dummy text of the printing and typesetting industry. Lorem Ipsum has been the industry's Lorem Ipsum is simply dummy text of the printing and typesetting industry. Lorem Ipsum has been the industry's Lorem Ipsum is simply dummy text of the printing and typesetting industry.</p><a>Read More...</a></div>
    </article>
  </div>
</section>

<section class="consult" role="img" aria-label="Open white doors looking out on the ocean and palm trees">
  <div class="door l"></div><div class="door r"></div>
  <div class="consult-head">
    <h2>Free Consultation</h2>
    <p>Enter your details below</p>
    <div class="chev"><svg width="20" height="12" viewBox="0 0 20 12"><path d="M2 2l8 8 8-8" fill="none" stroke="#fff" stroke-width="2.5"/></svg></div>
  </div>
  <div class="panel">
    <div class="panel-close"><svg width="12" height="12" viewBox="0 0 12 12"><path d="M1 1l10 10M11 1 1 11" stroke="#fff" stroke-width="2"/></svg></div>
    <p class="panel-intro">Tidal Pane Care, We are located in Grand Cayman, Cayman Islands. Our services include residencial interior and exterior window cleaning and commercial.</p>
    <div class="field active">Name</div>
    <div class="field">Mobile Number</div>
    <div class="field">Email Address</div>
    <div class="field">Ceiling Fans Cleaning<span class="drop"><svg width="10" height="6" viewBox="0 0 10 6"><path d="M0 0h10L5 6z" fill="#fff"/></svg></span></div>
    <div class="field">Duration<span class="drop"><svg width="10" height="6" viewBox="0 0 10 6"><path d="M0 0h10L5 6z" fill="#fff"/></svg></span></div>
    <p class="dates-label">Preferred Consultation Dates</p>
    <div class="submit-row"><span class="btn-submit">SUBMIT NOW</span><span>05/17/2015</span><span>To</span><span>05/17/2015</span></div>
  </div>
</section>

<section class="testimonials">
  <div class="wrap">
    <h2 class="sect-title">Client Testimonials</h2>
    <p class="sect-sub">Let me say right up front.</p>
    <div class="rule"></div>
    <div class="client-photo" role="img" aria-label="Portrait of a smiling client"></div>
    <div class="quote">
      <span class="quote-mark">&ldquo;</span>
      <p>Lorem Ipsum is simply dummy text of the printing and typesetting industry. Lorem Ipsum has been the industry's standard dummy text ever since the 1500s, when an unknown printer took a galley of type and scrambled.</p>
      <h4>Marisol Teague</h4>
      <small>President, Harbor Ledger Consultants, Inc.</small>
    </div>
    <div class="dots"><i></i><i></i><i></i><i class="on"></i></div>
  </div>
</section>

<section class="partners">
  <div class="wrap">
    <h2 class="sect-title">Our Partner</h2>
    <div class="rule"></div>
    <div class="p-arrow l"><svg width="8" height="12" viewBox="0 0 8 12"><path d="M6 1 1 6l5 5" fill="none" stroke="#fff" stroke-width="2"/></svg></div>
    <div class="p-arrow r"><svg width="8" height="12" viewBox="0 0 8 12"><path d="M2 1l5 5-5 5" fill="none" stroke="#fff" stroke-width="2"/></svg></div>
    <div class="partner-row">
      <div class="partner"><span></span>Corveline</div>
      <div class="partner"><span></span>Leafmere</div>
      <div class="partner"><span></span>Voltaris</div>
    </div>
  </div>
</section>

<section class="contact">
  <div class="wrap">
    <h2 class="sect-title">Contact</h2>
    <p class="sect-sub">Let's talk business, get in touch!</p>
    <div class="rule"></div>
    <div class="office">
      <h5>Office Hours</h5>
      <p>Monday to Friday / 7:00 - 18:00 Saturday / 9:00 - 15:00</p>
      <div class="row"><svg width="14" height="18" viewBox="0 0 14 18"><path d="M7 0a7 7 0 0 0-7 7c0 5 7 11 7 11s7-6 7-11a7 7 0 0 0-7-7zm0 10a3 3 0 1 1 0-6 3 3 0 0 1 0 6z" fill="#fff"/></svg><span>Tidal Pane Care, Grand Cayman, Cayman Islands</span></div>
      <div class="row"><svg width="14" height="14" viewBox="0 0 24 24"><path fill="#fff" d="M6.6 10.8a15 15 0 0 0 6.6 6.6l2.2-2.2c.3-.3.7-.4 1-.2 1.1.4 2.3.6 3.6.6.6 0 1 .4 1 1V20c0 .6-.4 1-1 1A17 17 0 0 1 3 4c0-.6.4-1 1-1h3.5c.6 0 1 .4 1 1 0 1.3.2 2.5.6 3.6.1.3 0 .7-.2 1z"/></svg><span>+345 555 0194</span></div>
      <div class="row"><svg width="14" height="11" viewBox="0 0 24 18"><rect x="1" y="1" width="22" height="16" fill="none" stroke="#fff" stroke-width="2"/><path d="M1 1l11 9 11-9" fill="none" stroke="#fff" stroke-width="2"/></svg><span>hello@tidalpanecare.ky</span></div>
      <div class="socials"><i></i><i></i><i></i></div>
    </div>
    <div class="cform">
      <div class="two"><div class="cinput">Name</div><div class="cinput">Email (will not published)</div></div>
      <div class="carea">Message</div>
      <span class="btn-send">Send</span>
    </div>
    <div class="to-top"><svg width="18" height="11" viewBox="0 0 18 11"><path d="M2 9l7-7 7 7" fill="none" stroke="#fff" stroke-width="2.5"/></svg></div>
  </div>
</section>

<footer class="site-footer">Copyright © Tidal Pane Care . All Rights Reserved</footer>

</body>
</html>
```